Postcard flyer for body postive dance classes

We need an eye catching double sided A6 postcard for body positive dance classes. The business name is twirlbrightday and already have a rough logo and some text that needs tidying up and putting together. The design needs to be simple and elegant. We are appealing to a diverse range of adult women with or without dance experience to join us in a safe, supportive and creative environment. We would like the design to use black, white and a soft green. The final design should communicate movement, contentment and wholeness. File with information attached.

Target Market(s)

Diverse range of adult women

Industry/Entity Type

Health And Wellness

Font styles to use
Other font styles liked:
• Candara or similar but open to suggestions

Colors
abd036
cadf82
eaf2ce
fffefb
fef9ed
fff3d1
ffffff

Requirements
Must have
• Logo and text provided.
Nice to have
• Sense of movement. Match to website colours and style.
Should not have
• Intimidating perfect body images

```html
<!DOCTYPE html>
<html lang="en">
<head>
<meta charset="utf-8">
<title>twirlbrightday – postcard</title>
<link href="https://fonts.googleapis.com/css2?family=Josefin+Sans:wght@300;400;600&family=Montserrat:wght@600;800&display=swap" rel="stylesheet">
<style>
  :root {
    --green: #abd036;
    --green-soft: #cadf82;
    --green-pale: #eaf2ce;
    --grey-band: #c4c4c2;
    --ink: #1e1e1e;
    --ink-soft: #4a4a4a;
    --paper: #ffffff;
    --stage: #e6e6e6;
  }
  * { box-sizing: border-box; margin: 0; padding: 0; }
  html, body { width: 1200px; height: 1200px; overflow: hidden; }
  body {
    background: var(--stage);
    font-family: "Josefin Sans", sans-serif;
    color: var(--ink);
    position: relative;
  }
  .card {
    position: absolute;
    left: 210px;
    width: 780px;
    height: 552px;
    background: var(--paper);
    overflow: hidden;
    box-shadow: 0 8px 24px rgba(0,0,0,.12);
  }
  .card--front { top: 32px; }
  .card--back {
    top: 616px;
    background: linear-gradient(135deg, #e4e4e4 0%, #f7f7f7 45%, #ffffff 100%);
  }

  /* front */
  .front-frame {
    position: absolute; left: 300px; top: 0; right: 20px; bottom: 20px;
    background: var(--green-pale);
  }
  .front-panel {
    position: absolute; left: 322px; top: 0; right: 20px; bottom: 44px;
    background: var(--paper);
  }
  .band { position: absolute; bottom: 20px; }
  .band--grey { left: 24px; width: 82px; top: 150px; background: var(--grey-band); }
  .band--green { left: 116px; width: 86px; top: 126px; background: var(--green-soft); }
  .band--pale { left: 212px; width: 82px; top: 102px; background: var(--green-pale); }
  .dancer {
    position: absolute; left: 60px; top: 250px; width: 230px; height: 282px;
    background: radial-gradient(ellipse at 55% 45%, #3a3a3a 0%, #6b6b6b 45%, rgba(120,120,120,0) 75%);
  }
  .headline {
    position: absolute; left: 340px; top: 30px; width: 410px;
    font-weight: 300; font-size: 56px; line-height: 1; letter-spacing: .5px;
  }
  .headline b {
    font-family: "Montserrat", sans-serif; font-weight: 800; color: var(--green);
  }
  .headline .line2 b { font-size: 50px; }
  .core-line {
    position: absolute; left: 340px; top: 168px; font-size: 23px; font-weight: 300;
    color: var(--ink-soft);
  }
  .celebration {
    position: absolute; left: 360px; top: 204px; right: 40px; height: 52px;
    background: var(--green-soft); color: var(--paper);
    font-family: "Montserrat", sans-serif; font-weight: 800; font-size: 14px;
    text-align: right; padding: 8px 14px; line-height: 1.3;
  }
  .group-photo {
    position: absolute; left: 470px; top: 262px; width: 280px; height: 150px;
    background: linear-gradient(180deg, #d4d4d4 0%, #ececec 60%, rgba(255,255,255,0) 100%);
  }
  .group-photo--back { left: 70px; top: 36px; width: 320px; height: 170px; }
  .brand {
    position: absolute; left: 420px; top: 408px; display: flex; align-items: center; gap: 12px;
  }
  .brand-dot { width: 40px; height: 40px; border-radius: 50%; border: 2px solid var(--ink); }
  .brand-name { font-size: 40px; font-weight: 400; line-height: 1; }
  .brand-tag { font-size: 13px; margin-top: 4px; color: var(--ink-soft); }
  .visit {
    position: absolute; left: 322px; right: 20px; bottom: 20px; height: 24px;
    background: var(--green-pale); font-size: 13px; letter-spacing: 1px;
    display: flex; align-items: center; justify-content: center; color: var(--ink-soft);
  }

  /* back */
  .stamp {
    position: absolute; right: 40px; top: 30px; width: 100px; height: 86px;
    border: 1px solid #c8c8c8; background: #ececec;
  }
  .intro-band {
    position: absolute; left: 40px; top: 200px; width: 390px; height: 26px;
    background: var(--green-pale); font-size: 19px; color: var(--ink-soft);
    padding: 4px 16px; letter-spacing: .3px;
  }
  .intro-copy {
    position: absolute; left: 56px; top: 232px; width: 370px;
    font-family: "Montserrat", sans-serif; font-weight: 800; font-size: 15px;
    line-height: 1.3; color: var(--ink-soft);
  }
  .contact-title {
    position: absolute; left: 56px; top: 330px;
    font-family: "Montserrat", sans-serif; font-weight: 800; font-size: 26px; color: var(--green);
    border-bottom: 2px solid var(--green-soft); padding-bottom: 2px;
  }
  .contact-list {
    position: absolute; left: 60px; top: 378px; list-style: none;
    font-size: 17px; line-height: 1.35; color: var(--ink-soft); font-weight: 300;
  }
  .visit--back { left: 40px; right: auto; width: 380px; bottom: 28px; justify-content: flex-start; padding-left: 14px; }
</style>
</head>
<body>

<section class="card card--front" aria-label="Postcard front">
  <div class="front-frame"></div>
  <div class="front-panel"></div>
  <div class="band band--grey"></div>
  <div class="band band--green"></div>
  <div class="band band--pale"></div>
  <div class="dancer" role="img" aria-label="Photo of a dancer in a black dress reaching upward"></div>

  <h1 class="headline">
    <div>Dance is <b>joy</b></div>
    <div class="line2"><b>Dance</b> is love</div>
  </h1>
  <p class="core-line">Dance is at the core of our being</p>
  <p class="celebration">a celebration of movement,<br>vitality and wholeness.</p>

  <div class="group-photo" role="img" aria-label="Photo of four smiling women in white t-shirts"></div>

  <div class="brand">
    <span class="brand-dot"></span>
    <div>
      <div class="brand-name">twirlbrightday</div>
      <div class="brand-tag">Movement, contentment, wholeness</div>
    </div>
  </div>

  <p class="visit">Please visit us at: www.twirlbrightday.com.au</p>
</section>

<section class="card card--back" aria-label="Postcard back">
  <div class="stamp"></div>
  <div class="group-photo group-photo--back" role="img" aria-label="Photo of four smiling women in white t-shirts"></div>

  <p class="intro-band">IF YOU'VE NEVER DANCED BEFORE</p>
  <p class="intro-copy">and always wanted to or you want to reignite your past love of dance, join us at twirlbrightday to start your journey.</p>

  <h2 class="contact-title">Contact us now!</h2>
  <ul class="contact-list">
    <li>E: maya@twirlbrightday.com.au</li>
    <li>P: 0400 418 276</li>
    <li>www.twirlbrightday.com.au</li>
    <li>Fernvale/Brookton</li>
  </ul>

  <p class="visit visit--back">Please visit us at: www.twirlbrightday.com.au</p>
</section>

</body>
</html>
```